Eye surgeon needs a presentation folder and a business card for his practice manager. Logo alread...

I need a folder to put papers in when I am scheduling patients for surgery. The information is general, such as costs, consent forms etc. The folder is designed to give the patient these papers in a neat manner. The cover of the folder needs to use my brand and perhaps create some interest when it is sitting on their kitchen bench with visitors and family. I'll attach a typical template for a folder. It needs to be stylish, classic and professional, as I am about to operate on the person's eye. <br/>I would like my logo included. I'll also attach a photo which is on my website which might work to wrap around the folder. The website address is raybelford.com.au and you can see the way the image is used there on most of the pages as a banner. My profile photo could possibly used as well. Perhaps on the back, but if it looks strange then that is not necessary. The contact information need not be on the folder. Just Dr Ray Belford, Ophthalmic Surgeon. Finally, our brand slogan is. "The world's a beautiful place, see it clearly". This could also be on it. Again, this all needs to be professional looking. <br/>I've attached all our previous design jobs, 2 profile pictures, and the image that I think would work. Please also look at the website. <br/><br/>The second part of the project is to create a business card for my practice manager. Her name is Miriam Holtby<br/>It should include<br/>Miriam Holtby (BCom)<br/>Practice Manager for Dr Ray Belford<br/>Ophthalmic Surgeon <br/><br/>Then all the details which are on our current business card<br/><br/><br/><br/><br/>

Contact Information for Business Card

Just match the business cards I already have, but use the details above

Colors

Designer to choose colors to be used in the design.

```html
<!DOCTYPE html>
<html lang="en">
<head>
<meta charset="utf-8">
<title>Dr Ray Belford – Presentation Folder and Business Card</title>
<link href="https://fonts.googleapis.com/css2?family=Open+Sans:wght@400;600;700;800&display=swap" rel="stylesheet">
<style>
:root{
  --canvas:#ebecee;
  --brand:#1f8fd8;
  --brand-dark:#146db3;
  --brand-light:#4fb0ee;
  --paper:#ffffff;
  --paper-shade:#f1f3f5;
  --ink:#3a3f45;
  --muted:#8a9098;
  --sun:#e9a24a;
  --sea:#2b3e52;
}
*{box-sizing:border-box;margin:0;padding:0}
html,body{width:833px;height:1200px;overflow:hidden}
body{background:var(--canvas);font-family:"Open Sans",Arial,sans-serif;color:var(--ink);position:relative}

.brand-mark{display:flex;align-items:center;gap:7px;color:var(--brand);font-weight:700;white-space:nowrap}
.brand-mark .dot{border-radius:50%;background:var(--brand);flex:none}

/* folder outer spread */
.folder-spread{position:absolute;left:76px;top:30px;width:680px;height:450px;display:flex;box-shadow:0 6px 18px rgba(0,0,0,.18)}
.folder-back{width:340px;height:100%;background:linear-gradient(160deg,var(--brand-light),var(--brand) 55%,var(--brand-dark));position:relative}
.profile{position:absolute;left:22px;bottom:26px;display:flex;align-items:flex-end;gap:10px}
.profile-photo{width:58px;height:70px;border:3px solid var(--paper);background:linear-gradient(180deg,#c9d6e0,#8ea3b4)}
.profile-name{color:var(--paper);font-size:9px;font-weight:700;line-height:1.35}
.profile-name span{display:block;font-weight:400;font-size:7px;opacity:.9}

.folder-front{width:340px;height:100%;background:var(--paper);position:relative;overflow:hidden}
.cover-photo{position:absolute;left:0;top:0;width:100%;height:250px;background:linear-gradient(180deg,#3d4b5c 0%,#7e6f62 38%,var(--sun) 52%,#6d6458 58%,var(--sea) 100%)}
.slogan{position:absolute;left:18px;top:182px;color:var(--paper);font-weight:800;font-size:15px;line-height:1.15;text-transform:uppercase;letter-spacing:.2px}
.cover-brand{position:absolute;left:0;right:0;top:268px;display:flex;flex-direction:column;align-items:center}
.cover-brand .brand-mark{font-size:20px}
.cover-brand .dot{width:22px;height:22px}
.cover-brand .role{font-size:8px;color:var(--muted);margin-top:4px;letter-spacing:.5px}
.cover-band{position:absolute;left:0;bottom:0;width:100%;height:92px;background:linear-gradient(180deg,var(--brand-light),var(--brand-dark))}

/* business cards */
.card{position:absolute;top:520px;width:240px;height:140px;box-shadow:0 4px 12px rgba(0,0,0,.18)}
.card-back{left:76px;background:linear-gradient(170deg,#3c4c5e,#b08660 45%,var(--brand) 46%,var(--brand-dark));display:flex;align-items:center;justify-content:center}
.card-back .brand-mark{color:var(--paper);font-size:15px}
.card-back .dot{width:16px;height:16px;background:var(--paper)}
.card-front{left:328px;background:var(--paper);padding:16px 16px}
.card-front .brand-mark{position:absolute;right:14px;top:14px;font-size:10px}
.card-front .dot{width:10px;height:10px}
.card-name{font-size:10px;font-weight:700;color:var(--brand-dark)}
.card-title{font-size:7px;line-height:1.4;margin-top:3px}
.card-contact{position:absolute;left:16px;bottom:14px;font-size:6.5px;line-height:1.6;color:var(--muted)}

.logo-block{position:absolute;left:588px;top:520px;width:168px;height:140px;display:flex;align-items:center;justify-content:center}
.logo-block .brand-mark{font-size:17px}
.logo-block .dot{width:26px;height:26px}

/* folder inside */
.folder-inside{position:absolute;left:76px;top:710px;width:680px;height:460px;display:flex;box-shadow:0 6px 18px rgba(0,0,0,.18)}
.inside-page{width:340px;height:100%;background:linear-gradient(90deg,var(--paper-shade),var(--paper));position:relative;overflow:hidden}
.inside-page.right{background:linear-gradient(90deg,var(--paper),var(--paper-shade))}
.pocket{position:absolute;left:0;bottom:0;width:100%;height:150px}
.pocket svg{display:block}
.pocket-mark{position:absolute;left:0;right:0;top:62px;display:flex;justify-content:center}
.pocket-mark .brand-mark{color:var(--brand-light);font-size:14px}
.pocket-mark .dot{width:14px;height:14px;background:var(--brand-light)}
.pocket-card{position:absolute;left:114px;top:34px;width:118px;height:66px;background:var(--paper);box-shadow:0 2px 6px rgba(0,0,0,.15);padding:8px}
.pocket-card .brand-mark{font-size:7px;gap:4px}
.pocket-card .dot{width:7px;height:7px}
.pocket-card p{font-size:5px;color:var(--muted);margin-top:5px;line-height:1.4}
</style>
</head>
<body>

<section class="folder-spread">
  <div class="folder-back">
    <div class="profile">
      <div class="profile-photo" role="img" aria-label="Portrait photo of Dr Ray Belford"></div>
      <p class="profile-name">Dr Ray Belford<span>Ophthalmic Surgeon</span></p>
    </div>
  </div>
  <div class="folder-front">
    <div class="cover-photo" role="img" aria-label="Photo of the sun setting over the sea"></div>
    <h1 class="slogan">The world's a<br>beautiful place<br>see it clearly</h1>
    <div class="cover-brand">
      <div class="brand-mark"><span class="dot"></span>Dr Ray Belford</div>
      <p class="role">Ophthalmic Surgeon</p>
    </div>
    <div class="cover-band"></div>
  </div>
</section>

<div class="card card-back" role="img" aria-label="Sunset photo behind the practice name">
  <div class="brand-mark"><span class="dot"></span>Dr Ray Belford</div>
</div>

<div class="card card-front">
  <div class="brand-mark"><span class="dot"></span>Dr Ray Belford</div>
  <p class="card-name">Miriam Holtby (BCom)</p>
  <p class="card-title">Practice Manager for Dr Ray Belford<br>Ophthalmic Surgeon</p>
  <p class="card-contact">T 02 5550 1842<br>F 02 5550 1843<br>E office@raybelford.com.au<br>raybelford.com.au</p>
</div>

<div class="logo-block">
  <div class="brand-mark"><span class="dot"></span>Dr Ray Belford</div>
</div>

<section class="folder-inside">
  <div class="inside-page left">
    <div class="pocket">
      <svg width="340" height="150" viewBox="0 0 340 150">
        <path d="M0 20 Q170 0 340 20 L340 150 L0 150 Z" fill="var(--brand)"/>
      </svg>
      <div class="pocket-mark"><div class="brand-mark"><span class="dot"></span>Dr Ray Belford</div></div>
    </div>
  </div>
  <div class="inside-page right">
    <div class="pocket">
      <svg width="340" height="150" viewBox="0 0 340 150">
        <path d="M0 20 Q170 0 340 20 L340 150 L0 150 Z" fill="var(--brand)"/>
      </svg>
      <div class="pocket-card">
        <div class="brand-mark"><span class="dot"></span>Dr Ray Belford</div>
        <p>Miriam Holtby (BCom)<br>Practice Manager</p>
      </div>
    </div>
  </div>
</section>

</body>
</html>
```